Musician looking for catchy Web Design for promotion

My name is Brenna Colfer. I'm an Irish musician who plays the tin whistle and the flute. I'm also the leader of a traditional Irish music and dance ensemble called Wander the Hillside (www.wanderthehillside-example.com) and for the past 30 years, I've toured the world performing thousands of concerts. I run an annual cruise (www.brennacolfervoyage-example.com) that I would like a link to, and I'm also I'm organizing tours to Ireland that I would like a page set up for. I'm looking for a website to promote my tours and my music.
Updates

Hello Graphic Designers, I am only looking for the design of the home page to make my decision. Thank you. Brenna

Target Market(s)

Music fans of Irlsh and World Music

Industry/Entity Type

Entertainment Industry

Number of Pages Required

5+ page

Requirements
Must have
• I'm looking for a catchy design that shows a photo of me. I would like a few links....
• BIO
• TOURDATES
• BRENNA COLFER CRUISE
• MUSICAL TOUR OF IRELAND
• CONTACT
• VIDEO
• GALLERY
• CONTACT
• MAILING LIST
• STORE
Nice to have
• we'll see!

```html
<!DOCTYPE html>
<html lang="en">
<head>
<meta charset="utf-8">
<title>Brenna Colfer's Musical Tour of Ireland</title>
<link href="https://fonts.googleapis.com/css2?family=PT+Sans:ital,wght@0,400;0,700;1,400;1,700&display=swap" rel="stylesheet">
<style>
  :root {
    --red: #9b2219;
    --red-bright: #e0352a;
    --ink: #2a2a2a;
    --body: #5a5a5a;
    --page: #f3f2f0;
    --card: #cccccc;
    --footer: #333333;
    --footer-text: #a9a9a9;
    --footer-head: #9a9a9a;
    --bar: #000000;
  }
  * { box-sizing: border-box; margin: 0; padding: 0; }
  html, body { width: 960px; height: 1200px; overflow: hidden; background: #fff; }
  body { font-family: "PT Sans", Arial, sans-serif; position: relative; color: var(--ink); }

  .site-header { position: absolute; left: 0; top: 0; width: 960px; height: 100px; background: #fff; }
  .brand { position: absolute; left: 112px; top: 43px; display: flex; align-items: center; gap: 9px; }
  .brand-mark { width: 12px; height: 12px; background: var(--ink); }
  .brand-name { font-size: 13px; font-weight: 400; color: var(--ink); line-height: 13px; letter-spacing: 0.2px; }

  .main-nav { position: absolute; top: 0; left: 447px; height: 100px; }
  .main-nav a { position: absolute; top: 0; height: 100px; line-height: 100px; font-size: 12px; color: #444; text-decoration: none; letter-spacing: 0.6px; text-transform: uppercase; white-space: nowrap; }
  .main-nav .active { left: 0; width: 112px; background: var(--red); color: #fff; font-weight: 700; text-align: center; }
  .nav-gallery { left: 128px; }
  .nav-bio { left: 203px; }
  .nav-tour { left: 308px; }
  .nav-contact { left: 421px; }

  .content { position: absolute; left: 0; top: 100px; width: 960px; height: 758px; background: var(--page); }
  .section-title { position: absolute; left: 105px; top: 30px; font-size: 30px; font-weight: 700; letter-spacing: 2px; color: var(--ink); }
  .title-rule { position: absolute; left: 333px; top: 47px; width: 558px; height: 4px; background: var(--red); }

  .feature-card { position: absolute; left: 92px; width: 802px; height: 188px; background: var(--card); }
  .feature-photo { position: absolute; left: 12px; top: 10px; width: 162px; height: 166px; }
  .photo-portrait { background: linear-gradient(160deg, #b7822f 0%, #9c6a2a 35%, #5a3a22 65%, #2b1e18 100%); }
  .photo-landscape { background: linear-gradient(180deg, #a9a48a 0%, #7d8a5a 45%, #4f6236 100%); }
  .photo-voyage { background: linear-gradient(180deg, #b9c4c8 0%, #7f97a3 50%, #4b6373 100%); }
  .feature-text { position: absolute; left: 210px; top: 22px; width: 568px; }
  .feature-name { font-size: 26px; font-weight: 700; color: var(--red); letter-spacing: 0.8px; line-height: 30px; }
  .feature-name em { font-style: italic; letter-spacing: 0; }
  .feature-summary { margin-top: 4px; font-size: 13.3px; line-height: 16.4px; color: var(--body); }
  .read-more { display: inline-block; margin-top: 13px; font-size: 13px; font-weight: 700; font-style: italic; color: var(--red); text-decoration: none; letter-spacing: 1px; }

  .site-footer { position: absolute; left: 0; top: 858px; width: 960px; height: 262px; background: var(--footer); }
  .footer-col { position: absolute; top: 51px; }
  .footer-col h3 { font-size: 20px; font-weight: 700; color: var(--footer-head); margin-bottom: 16px; }
  .footer-about { left: 79px; width: 240px; }
  .footer-about p { font-size: 12.3px; line-height: 15.3px; color: var(--footer-text); margin-bottom: 15px; }
  .footer-links { left: 367px; }
  .footer-links ul { list-style: none; }
  .footer-links li { display: flex; align-items: center; gap: 11px; font-size: 15.2px; line-height: 18.7px; color: var(--footer-text); }
  .footer-links svg { width: 15px; height: 13px; flex: none; }
  .footer-contact { left: 649px; width: 240px; }
  .footer-contact p { font-size: 13px; line-height: 16.5px; color: var(--footer-text); }
  .footer-contact .label { color: var(--red-bright); font-weight: 700; font-style: normal; }
  .footer-contact .address { font-style: italic; margin-bottom: 16px; }

  .copyright-bar { position: absolute; left: 0; top: 1120px; width: 960px; height: 38px; background: var(--bar); }
  .copyright-bar p { position: absolute; left: 74px; top: 12px; font-size: 10px; color: #8a8a8a; }
</style>
</head>
<body>
  <header class="site-header">
    <div class="brand">
      <span class="brand-mark"></span>
      <span class="brand-name">BRENNA COLFER'S<br>MUSICAL TOUR OF IRELAND</span>
    </div>
    <nav class="main-nav">
      <a class="active" href="#">About Brenna</a>
      <a class="nav-gallery" href="#">Gallery</a>
      <a class="nav-bio" href="#">Biographies</a>
      <a class="nav-tour" href="#">Musical Tour</a>
      <a class="nav-contact" href="#">Contact</a>
    </nav>
  </header>

  <main class="content">
    <h1 class="section-title">BIOGRAPHIES</h1>
    <div class="title-rule"></div>

    <article class="feature-card" style="top:105px">
      <div class="feature-photo photo-portrait" role="img" aria-label="Portrait of Brenna Colfer holding a flute"></div>
      <div class="feature-text">
        <h2 class="feature-name">BRENNA <em>Colfer</em></h2>
        <p class="feature-summary">BRENNA COLFER is considered one of the greatest musicians and personalities in the history of Irish music in America. She plays the tin whistle and flute and leads the ensemble Wander the Hillside, touring the world for over thirty years.</p>
        <a class="read-more" href="#">READ BIO &gt;&gt;</a>
      </div>
    </article>

    <article class="feature-card" style="top:309px">
      <div class="feature-photo photo-landscape" role="img" aria-label="Photo of the Irish countryside visited on the musical tour"></div>
      <div class="feature-text">
        <h2 class="feature-name">MUSICAL <em>Tour</em></h2>
        <p class="feature-summary">Travel with Brenna on her Musical Tour of Ireland, with nightly sessions, concerts and dance in the towns where the music was born. See the upcoming tour dates and reserve a place on the next journey.</p>
        <a class="read-more" href="#">TOUR DATES &gt;&gt;</a>
      </div>
    </article>

    <article class="feature-card" style="top:513px">
      <div class="feature-photo photo-voyage" role="img" aria-label="Photo of the cruise ship at sea"></div>
      <div class="feature-text">
        <h2 class="feature-name">BRENNA <em>Colfer Cruise</em></h2>
        <p class="feature-summary">Each year Brenna hosts a cruise full of Irish music, with concerts, workshops and late night sessions at sea. Find the sailing dates and cabins at www.brennacolfervoyage-example.com and join the crew.</p>
        <a class="read-more" href="#">VISIT THE CRUISE &gt;&gt;</a>
      </div>
    </article>
  </main>

  <footer class="site-footer">
    <section class="footer-col footer-about">
      <h3>About Us</h3>
      <p>Lorem ipsum dolor sit amet, consectetur adipiscing elit. Etiam malesuada, elit nec laoreet aliquam, arcu justo ultricies ante.</p>
      <p>Quisque dignissim mi quis luctus dapibus nec efficitur nibh sapien id sapien.</p>
    </section>
    <section class="footer-col footer-links">
      <h3>Quick Links</h3>
      <ul>
        <li><svg viewBox="0 0 15 13"><path d="M1 7 L5.5 11.5 L14 1.5" fill="none" stroke="#e0352a" stroke-width="3" stroke-linecap="round" stroke-linejoin="round"/></svg>Latest News</li>
        <li><svg viewBox="0 0 15 13"><path d="M1 7 L5.5 11.5 L14 1.5" fill="none" stroke="#e0352a" stroke-width="3" stroke-linecap="round" stroke-linejoin="round"/></svg>Tour Dates</li>
        <li><svg viewBox="0 0 15 13"><path d="M1 7 L5.5 11.5 L14 1.5" fill="none" stroke="#e0352a" stroke-width="3" stroke-linecap="round" stroke-linejoin="round"/></svg>Store</li>
        <li><svg viewBox="0 0 15 13"><path d="M1 7 L5.5 11.5 L14 1.5" fill="none" stroke="#e0352a" stroke-width="3" stroke-linecap="round" stroke-linejoin="round"/></svg>Video</li>
        <li><svg viewBox="0 0 15 13"><path d="M1 7 L5.5 11.5 L14 1.5" fill="none" stroke="#e0352a" stroke-width="3" stroke-linecap="round" stroke-linejoin="round"/></svg>Gallery</li>
        <li><svg viewBox="0 0 15 13"><path d="M1 7 L5.5 11.5 L14 1.5" fill="none" stroke="#e0352a" stroke-width="3" stroke-linecap="round" stroke-linejoin="round"/></svg>Musical Tour</li>
        <li><svg viewBox="0 0 15 13"><path d="M1 7 L5.5 11.5 L14 1.5" fill="none" stroke="#e0352a" stroke-width="3" stroke-linecap="round" stroke-linejoin="round"/></svg>Brenna Colfer Cruise</li>
        <li><svg viewBox="0 0 15 13"><path d="M1 7 L5.5 11.5 L14 1.5" fill="none" stroke="#e0352a" stroke-width="3" stroke-linecap="round" stroke-linejoin="round"/></svg>Mailing List</li>
      </ul>
    </section>
    <section class="footer-col footer-contact">
      <h3>Contact Us</h3>
      <p class="address"><span class="label">Address:</span>&nbsp; Lorem ipsum dolor sit amet, consectetur adipiscing elit</p>
      <p><span class="label">Phone:</span> 1-800-555-0147</p>
      <p><span class="label">Email:</span> hello@example.com</p>
    </section>
  </footer>

  <div class="copyright-bar"><p>© Copyright 2016 . All Rights Reserved.</p></div>
</body>
</html>
```